Letterhead and Business card for Construction company

We need a letterhead and business card with our new company logo. We are based in NY. We develop and build properties.

The design should incorporate some unique feature from the logo (shape, font...). it should look like an extension from it.

Design should be clean and elegant, professional, not too busy.

The letterhead should include:
Logo (attached)
Address
Phone
Email

Please find the attached logo images and AI file.

Target Market(s)

Construction industry professionals

Industry/Entity Type

Construction, Development

Font styles to use
Sans Serif

Colors

Designer to choose colors to be used in the design.

Requirements
Must have
• Design should incorporate logo elements, additional assets are welcome. I'd like to see some other shapes / images invorporated too.

```html
<!DOCTYPE html>
<html lang="en">
<head>
<meta charset="utf-8">
<title>Meridian Stone Works – Stationery</title>
<link href="https://fonts.googleapis.com/css2?family=Exo+2:wght@300;400;600;700;800&display=swap" rel="stylesheet">
<style>
  :root {
    --orange: #f47b20;
    --ink: #111111;
    --dark: #1e1e1e;
    --paper: #ffffff;
    --shadow: 12px 12px 14px rgba(40, 20, 0, 0.55);
  }
  * { box-sizing: border-box; margin: 0; padding: 0; }
  html, body {
    width: 920px; height: 1200px; overflow: hidden;
    background: var(--orange);
    font-family: "Exo 2", sans-serif;
    color: var(--ink);
  }
  .canvas { position: relative; width: 920px; height: 1200px; }
  .sheet { position: absolute; background: var(--paper); box-shadow: var(--shadow); }

  .card-front { left: 59px; top: 41px; width: 381px; height: 217px; }
  .card-back  { left: 480px; top: 41px; width: 380px; height: 217px; }
  .letterhead { left: 60px; top: 294px; width: 800px; height: 866px; }

  /* wordmark in place of the brand mark */
  .wordmark {
    position: absolute; color: var(--orange); font-weight: 800;
    display: flex; align-items: center; gap: 6px; line-height: 1;
    letter-spacing: 0.02em;
  }
  .wordmark .mark-square { background: var(--orange); flex: none; }
  .wordmark .name { display: flex; flex-direction: column; }
  .wordmark .name small { font-size: 0.42em; letter-spacing: 0.08em; margin-top: 3px; font-weight: 800; }

  .card-front .wordmark { left: 190px; top: 111px; transform: translate(-50%, -50%); font-size: 30px; }
  .card-front .wordmark .mark-square { width: 12px; height: 12px; }
  .card-back .wordmark { left: 107px; top: 111px; transform: translate(-50%, -50%); font-size: 30px; }
  .card-back .wordmark .mark-square { width: 12px; height: 12px; }
  .letterhead .wordmark { left: 46px; top: 52px; font-size: 46px; }
  .letterhead .wordmark .mark-square { width: 18px; height: 18px; }

  .card-front .web {
    position: absolute; left: 0; width: 100%; top: 182px;
    text-align: center; font-size: 10.5px; font-weight: 400;
  }
  .card-front .split-bar {
    position: absolute; left: 47px; top: 199px; width: 287px; height: 4px;
    border-radius: 2px; overflow: hidden;
    background: linear-gradient(100deg, var(--orange) 0 49%, var(--dark) 49% 100%);
  }

  .person { position: absolute; left: 206px; top: 52px; display: flex; gap: 6px; align-items: center; }
  .person svg { width: 19px; height: 20px; }
  .person .who { line-height: 1; }
  .person .who strong { display: block; font-size: 10px; font-weight: 700; }
  .person .who span { font-size: 9px; font-weight: 400; }

  .contact { position: absolute; display: flex; }
  .contact .icons {
    background: var(--dark); border-radius: 5px;
    display: flex; flex-direction: column; justify-content: space-around; align-items: center;
  }
  .contact .icons svg { fill: var(--orange); }
  .contact ul { list-style: none; display: flex; flex-direction: column; justify-content: space-around; }

  .card-back .contact { left: 206px; top: 112px; height: 54px; }
  .card-back .contact .icons { width: 19px; padding: 3px 0; }
  .card-back .contact .icons svg { width: 8px; height: 8px; }
  .card-back .contact ul { margin-left: 5px; font-size: 9px; line-height: 1; }

  .letterhead .contact { left: 62px; top: 762px; height: 52px; }
  .letterhead .contact .icons { width: 19px; padding: 3px 0; }
  .letterhead .contact .icons svg { width: 8px; height: 8px; }
  .letterhead .contact ul { margin-left: 6px; font-size: 11px; line-height: 1; }

  .company-title { position: absolute; left: 282px; top: 64px; width: 445px; }
  .company-title h1 {
    font-size: 38px; font-weight: 700; letter-spacing: 0.005em; line-height: 1;
    white-space: nowrap;
  }
  .company-title .subline { display: flex; align-items: center; margin-top: 4px; }
  .company-title p { font-size: 19px; font-weight: 300; white-space: nowrap; line-height: 1; }
  .company-title .rule { flex: 1; height: 2px; background: var(--ink); margin-left: 12px; }

  .side-bar { position: absolute; left: 765px; top: 13px; width: 17px; height: 836px; }
  .footer-rule {
    position: absolute; left: 65px; top: 747px; width: 671px; height: 5px;
    border-radius: 3px; background: var(--orange);
  }
</style>
</head>
<body>
<div class="canvas">

  <svg width="0" height="0" style="position:absolute">
    <defs>
      <symbol id="i-phone" viewBox="0 0 10 10"><path d="M3 0h4a1 1 0 0 1 1 1v8a1 1 0 0 1-1 1H3a1 1 0 0 1-1-1V1a1 1 0 0 1 1-1zm0 1.5v6.5h4V1.5z"/></symbol>
      <symbol id="i-mail" viewBox="0 0 10 10"><path d="M0 2h10v6H0zm1 1 4 3 4-3z" fill-rule="evenodd"/></symbol>
      <symbol id="i-web" viewBox="0 0 10 10"><path d="M5 0a5 5 0 1 0 0 10A5 5 0 0 0 5 0zm0 1c.6.6 1 1.9 1.1 3.5H3.9C4 2.9 4.4 1.6 5 1zM1.1 4.5a4 4 0 0 1 2-3A7 7 0 0 0 2.9 4.5zm0 1h1.8a7 7 0 0 0 .2 3 4 4 0 0 1-2-3zM5 9c-.6-.6-1-1.9-1.1-3.5h2.2C6 7.1 5.6 8.4 5 9zm1.9-.5a7 7 0 0 0 .2-3h1.8a4 4 0 0 1-2 3zm.2-4a7 7 0 0 0-.2-3 4 4 0 0 1 2 3z"/></symbol>
      <symbol id="i-home" viewBox="0 0 10 10"><path d="M5 .5 0 5h1.5v4.5h2.5V6.5h2v3h2.5V5H10z"/></symbol>
    </defs>
  </svg>

  <section class="sheet card-front">
    <div class="wordmark"><span class="mark-square"></span><span class="name">MSW<small>CONTRACTING</small></span></div>
    <p class="web">www.meridianstone.com</p>
    <div class="split-bar"></div>
  </section>

  <section class="sheet card-back">
    <div class="wordmark"><span class="mark-square"></span><span class="name">MSW<small>CONTRACTING</small></span></div>
    <div class="person">
      <svg viewBox="0 0 19 20" fill="#f47b20"><circle cx="9.5" cy="5" r="5"/><path d="M0 20c0-6 4-9 9.5-9S19 14 19 20z"/></svg>
      <div class="who"><strong>MR. AARON VALE</strong><span>Founder &amp; CEO</span></div>
    </div>
    <div class="contact">
      <div class="icons">
        <svg><use href="#i-phone"/></svg><svg><use href="#i-mail"/></svg><svg><use href="#i-web"/></svg><svg><use href="#i-home"/></svg>
      </div>
      <ul>
        <li>555 0140 2298</li>
        <li>info@meridianstone</li>
        <li>www.meridianstone.com</li>
        <li>48 Harbor Ave, Zipcode 4120</li>
      </ul>
    </div>
  </section>

  <section class="sheet letterhead">
    <div class="wordmark"><span class="mark-square"></span><span class="name">MSW<small>CONTRACTING</small></span></div>
    <header class="company-title">
      <h1>MERIDIAN STONE WORKS</h1>
      <div class="subline"><p>CONTRACTING COMPANY LIMITED</p><span class="rule"></span></div>
    </header>

    <svg class="side-bar" viewBox="0 0 17 836" aria-hidden="true">
      <defs><clipPath id="bar-clip"><rect width="17" height="836" rx="8.5"/></clipPath></defs>
      <g clip-path="url(#bar-clip)">
        <rect width="17" height="836" fill="#000"/>
        <polygon points="0,0 17,0 17,410 0,426" fill="#f47b20"/>
      </g>
    </svg>

    <div class="footer-rule"></div>
    <div class="contact">
      <div class="icons">
        <svg><use href="#i-phone"/></svg><svg><use href="#i-mail"/></svg><svg><use href="#i-web"/></svg><svg><use href="#i-home"/></svg>
      </div>
      <ul>
        <li>555 0140 2298</li>
        <li>info@meridianstone</li>
        <li>www.meridianstone.com</li>
        <li>48 Harbor Ave, Zipcode 4120</li>
      </ul>
    </div>
  </section>

</div>
</body>
</html>
```